Logo + Label Design (Men’s Grooming Brand & Product Packaging)

Design a logo and 2 oz pomade label for Brant, a modern men’s grooming brand focused on clean, high-quality, natural ingredients. The design should establish a bold, masculine, minimalist identity that can later extend to products like shaving gel and body wash.

Key Requirements

Create a primary logo for “Brant” and a core label for the 2 oz pomade jar (screw-top).

Use a clean, modern style — masculine, confident, and approachable (think Wendel’s, Valto, Northfield Mill).

Design for 1–2 color screen printing on solid jar colors (white, black, or navy).

Avoid gradients, foil, or embossing. Must work in black & white.

Provide: vector logo, mockup of the 2 oz jar, color palette (CMYK/RGB/HEX), and font specs.

Winning design may lead to future projects (body wash, shave gel, skincare lines).

Font styles to use
Other font styles liked:
• We like the fonts and design concept in the attached mockup.

Requirements
Should not have
• We want to avoid too much writing or busy designs. We want to avoid having graphics/illustrations embedded in the logo if they will cause the brand to look less classy or sophisticated. We also want the design to look simple and all-American (e.g. Pellham and Stroud, Tall Pine, The BRIM, etc). We’d like to give a Kessler & Dunmore vibe that feels classy and high end.

```html
<!DOCTYPE html>
<html lang="en">
<head>
<meta charset="utf-8">
<title>Brant Hair Pomade Label</title>
<link href="https://fonts.googleapis.com/css2?family=Montserrat:wght@500;600;700&family=Open+Sans:wght@400;600&display=swap" rel="stylesheet">
<style>
  :root {
    --ink: #050505;
    --paper: #ffffff;
    --rule: 1.5px solid var(--paper);
    --head: "Montserrat", Arial, sans-serif;
    --body: "Open Sans", Arial, sans-serif;
  }
  * { box-sizing: border-box; margin: 0; padding: 0; }
  html, body { width: 1200px; height: 1000px; overflow: hidden; background: var(--ink); }
  .canvas { position: relative; width: 1200px; height: 1000px; overflow: hidden; background: var(--ink); color: var(--paper); }

  /* Large brand wordmarks */
  .wordmark {
    position: absolute;
    font-family: var(--head);
    font-weight: 700;
    font-size: 230px;
    line-height: 1;
    letter-spacing: -4px;
    white-space: nowrap;
    transform: translate(-50%, -50%) rotate(var(--turn));
  }
  .wordmark--left { left: 365px; top: 300px; --turn: 200deg; }
  .wordmark--right { left: 1270px; top: 190px; --turn: 20.5deg; }
  .reg-dot { position: absolute; left: 28px; top: 325px; width: 36px; height: 36px; border: 3px solid var(--paper); border-radius: 50%; }

  /* Angled tag */
  .tag {
    position: absolute;
    transform-origin: 0 0;
    display: grid;
    grid-template-columns: 370px 170px;
    grid-template-rows: 50px 50px;
    border-top: var(--rule);
    border-left: var(--rule);
    font-family: var(--head);
    white-space: nowrap;
  }
  .tag--top { left: 695px; top: 180px; transform: rotate(200deg); }
  .tag--right { left: 790px; top: 345px; transform: rotate(20.5deg); }
  .tag > div { border-right: var(--rule); border-bottom: var(--rule); padding: 0 14px; display: flex; align-items: center; }
  .tag__title { font-size: 37px; font-weight: 700; letter-spacing: 0.5px; padding-top: 6px !important; }
  .tag__scent { font-size: 25px; font-weight: 500; }
  .tag__size { font-size: 28px; font-weight: 600; }
  .tag__finish { flex-direction: column; align-items: flex-start !important; justify-content: center; font-size: 18px; font-weight: 500; line-height: 1.15; }
  .tag__finish span:first-child { border-bottom: var(--rule); }

  /* Flat label strip */
  .strip { position: absolute; display: flex; gap: 2px; height: 133px; white-space: nowrap; }
  .strip--upper { left: -708px; top: 610px; }
  .strip--lower { left: 90px; top: 800px; }
  .strip__main {
    display: grid;
    grid-template-columns: 395px 295px 100px 733px;
    grid-template-rows: 66px 67px;
    border-top: var(--rule);
    border-left: var(--rule);
  }
  .strip__main > div { border-right: var(--rule); border-bottom: var(--rule); }
  .cell-title { display: flex; align-items: center; justify-content: center; font: 700 38px/1 var(--head); letter-spacing: 0.5px; }
  .cell-scent { display: flex; align-items: center; justify-content: center; font: 500 22px/1 var(--head); letter-spacing: 0.5px; }
  .cell-hold { display: flex; flex-direction: column; align-items: center; justify-content: center; font: 500 15px/1.35 var(--head); }
  .cell-hold span:first-child { text-decoration: underline; text-underline-offset: 3px; }
  .cell-size { display: flex; flex-direction: column; align-items: center; justify-content: center; font: 500 20px/1 var(--head); }
  .cell-size small { font-size: 15px; }
  .cell-claims { grid-column: 2 / span 2; display: grid; grid-template-rows: repeat(3, 1fr); }
  .cell-claims p { font: 500 13px/1 var(--head); padding: 0 14px; display: flex; align-items: center; border-bottom: var(--rule); }
  .cell-claims p:last-child { border-bottom: 0; }
  .cell-text { padding: 6px 7px; font: 400 13px/1.45 var(--body); white-space: normal; overflow: hidden; }
  .cell-text h3 { font: 700 13px/1.3 var(--head); }
  .strip__maker { width: 162px; border: var(--rule); padding: 6px 10px; font-family: var(--head); }
  .strip__maker h3 { font-size: 13px; font-weight: 700; margin-bottom: 8px; }
  .strip__maker .maker-name { font-size: 21px; font-weight: 600; line-height: 1.12; }
  .strip__maker .maker-address { font-size: 13px; font-weight: 600; margin-top: 2px; }
</style>
</head>
<body>
<main class="canvas">

  <div class="tag tag--top">
    <div class="tag__title">HAIR POMADE</div>
    <div class="tag__size">2oz (57g)</div>
    <div class="tag__scent">FRESH &amp; CLEAN</div>
    <div class="tag__finish"><span>medium hold</span><span>matte finish</span></div>
  </div>

  <div class="wordmark wordmark--left">brant</div>
  <div class="reg-dot" aria-hidden="true"></div>
  <div class="wordmark wordmark--right">brant</div>

  <div class="tag tag--right">
    <div class="tag__title">HAIR POMADE</div>
    <div class="tag__size">2oz (57g)</div>
    <div class="tag__scent">FRESH &amp; CLEAN</div>
    <div class="tag__finish"><span>medium hold</span><span>matte finish</span></div>
  </div>

  <section class="strip strip--upper">
    <div class="strip__main">
      <div class="cell-title">HAIR POMADE</div>
      <div class="cell-hold"><span>MEDIUM HOLD</span><span>MATTE FINISH</span></div>
      <div class="cell-size">2 OZ<small>(57 G)</small></div>
      <div class="cell-text"><h3>DIRECTIONS:</h3>Melt small amount of pomade between hands before massaging into damp hair (for sleeker look) or dry hair (for more texture). Style as desired. For external use only.&nbsp; Avoid contact with eyes. If irritation occurs, discontinue use.</div>
      <div class="cell-scent">FRESH &amp; CLEAN</div>
      <div class="cell-claims"><p>NATURALLY DERIVED PLANT &amp; BEE-BASED INGREDIENTS</p><p>ALCOHOL FREE, NON-IRRITATING</p><p>FORMULATED TO MINIMIZE SCALP IRRITATION</p></div>
      <div class="cell-text"><h3>INGREDIENTS:</h3>Butyrospermum Parkii (Shea Butter), Cera Alba (Beeswax), Polyglycerol-3 Beeswax (Cera Bellina), Caprylic/Capric Triglyceride (Fractionated Coconut Oil), Tocopherol (Vitamin E), Fragrance (Parfum)</div>
    </div>
    <div class="strip__maker">
      <h3>MANUFACTURED BY:</h3>
      <p class="maker-name">Brant<br>Health<br>Products</p>
      <p class="maker-address">Millbrook, NC 28190</p>
    </div>
  </section>

  <section class="strip strip--lower">
    <div class="strip__main">
      <div class="cell-title">HAIR POMADE</div>
      <div class="cell-hold"><span>MEDIUM HOLD</span><span>MATTE FINISH</span></div>
      <div class="cell-size">2 OZ<small>(57 G)</small></div>
      <div class="cell-text"><h3>DIRECTIONS:</h3>Melt small amount of pomade between hands before massaging into damp hair (for sleeker look) or dry hair (for more texture). Style as desired. For external use only.&nbsp; Avoid contact with eyes. If irritation occurs, discontinue use.</div>
      <div class="cell-scent">FRESH &amp; CLEAN</div>
      <div class="cell-claims"><p>NATURALLY DERIVED PLANT &amp; BEE-BASED INGREDIENTS</p><p>ALCOHOL FREE, NON-IRRITATING</p><p>FORMULATED TO MINIMIZE SCALP IRRITATION</p></div>
      <div class="cell-text"><h3>INGREDIENTS:</h3>Butyrospermum Parkii (Shea Butter), Cera Alba (Beeswax), Polyglycerol-3 Beeswax (Cera Bellina), Caprylic/Capric Triglyceride (Fractionated Coconut Oil), Tocopherol (Vitamin E), Fragrance (Parfum)</div>
    </div>
    <div class="strip__maker">
      <h3>MANUFACTURED BY:</h3>
      <p class="maker-name">Brant<br>Health<br>Products</p>
      <p class="maker-address">Millbrook, NC 28190</p>
    </div>
  </section>

</main>
</body>
</html>
```